Website for Company that serves and supports Investment Banks

We are seeking to have a six page website that provides a basic description of our company's services. Our company provides Financial Models and Investment Memos on an outsourced basis to Small Investment Banks and Investment firms. We do not require a shopping cart. We already have a logo attached.

Target Market(s)

Small, regional investment banks. Small private equity firms.

Industry/Entity Type

Finance And Accounting

Coding

Coded - Design and coding required

Number of Pages Required

5+ page

Requirements
Nice to have
• Please use the logo design to drive how you design the layout for the website

```html
<!DOCTYPE html>
<html lang="en">
<head>
<meta charset="utf-8">
<title>LedgerPeak Analysts</title>
<link href="https://fonts.googleapis.com/css2?family=Josefin+Sans:wght@300;400;600;700&family=Montserrat:wght@400;500;600;700&family=Playfair+Display:wght@400;500&display=swap" rel="stylesheet">
<style>
:root{
  --navy:#123a6b;
  --navy-dark:#0c2748;
  --ink:#1e1e1e;
  --text:#6d6d6d;
  --muted:#9a9a9a;
  --line:#d9d9d9;
  --soft:#f2f3f5;
  --white:#ffffff;
  --grey-btn:#505050;
  --red:#c8232c;
}
*{box-sizing:border-box;margin:0;padding:0}
html,body{width:1200px;height:4724px;overflow:hidden}
body{position:relative;background:var(--white);font-family:"Josefin Sans",sans-serif;color:var(--ink)}
section,header,footer{position:absolute;left:0;width:1200px}
.btn{display:inline-block;font-family:"Montserrat",sans-serif;font-size:15px;font-weight:500;text-transform:uppercase;letter-spacing:.5px;text-align:center}

/* header */
.site-header{top:0;height:132px;background:var(--white)}
.brand{position:absolute;left:78px;top:14px;width:330px;text-align:center}
.brand-dot{width:58px;height:58px;border-radius:50%;background:var(--navy);margin:0 auto 6px}
.brand-name{font-family:"Montserrat",sans-serif;font-weight:700;font-size:21px;color:var(--navy);letter-spacing:.3px}
.brand-tag{font-family:"Montserrat",sans-serif;font-size:10px;color:var(--navy);letter-spacing:1px}
.top-mail{position:absolute;left:660px;top:10px;font-family:"Montserrat",sans-serif;font-size:14px;color:var(--text);display:flex;align-items:center;gap:8px}
.top-phone{position:absolute;left:912px;top:0;width:210px;height:54px;background:var(--navy);border-radius:0 0 8px 8px;color:var(--white);font-family:"Montserrat",sans-serif;font-weight:600;font-size:22px;display:flex;align-items:center;justify-content:center;gap:10px}
.main-nav{position:absolute;left:452px;top:84px;display:flex;gap:56px;font-family:"Montserrat",sans-serif;font-size:14px;color:var(--muted);text-transform:uppercase}
.main-nav .active{color:var(--ink)}

/* hero */
.hero{top:132px;height:577px;background:linear-gradient(100deg,#2c3440 0%,#4f5a66 35%,#a9b4be 60%,#37404c 100%)}
.hero h1{position:absolute;left:80px;top:160px;font-family:"Montserrat",sans-serif;font-weight:700;font-size:46px;color:var(--white)}
.hero p{position:absolute;left:80px;top:232px;width:680px;font-family:"Montserrat",sans-serif;font-size:20px;line-height:28px;color:var(--white)}
.hero .btn{position:absolute;left:80px;top:308px;width:212px;height:52px;line-height:52px;background:var(--white);color:var(--ink);border-radius:3px}

/* welcome */
.welcome{top:709px;height:378px;text-align:center}
.welcome h2{margin-top:52px;font-size:40px;font-weight:400}
.welcome p{width:850px;margin:0 auto;font-family:"Montserrat",sans-serif;font-size:13.5px;line-height:20px;color:var(--muted)}
.welcome .lead{margin-top:22px}
.welcome .gap{margin-top:14px}
.welcome .btn{margin-top:28px;width:262px;height:52px;line-height:52px;background:var(--navy);color:var(--white)}

/* pricing */
.pricing{top:1087px;height:535px}
.plan{position:absolute;top:47px;width:316px;height:426px;border:1px solid #e6e6e6;background:var(--white);text-align:center}
.plan.featured{top:38px;height:440px;border:none;box-shadow:0 4px 22px rgba(0,0,0,.18)}
.plan .price{margin-top:38px;font-family:"Montserrat",sans-serif;font-weight:700;font-size:42px}
.plan .tag{display:inline-block;margin-top:16px;width:230px;height:40px;line-height:40px;background:var(--navy);color:var(--white);font-family:"Montserrat",sans-serif;font-size:16px;font-weight:500}
.plan ul{list-style:none;margin:8px 24px 0}
.plan li{font-family:"Montserrat",sans-serif;font-size:15px;color:var(--text);padding:16px 0;border-bottom:1px solid #ececec}
.plan li:last-child{border-bottom:none}
.plan .details{position:absolute;left:78px;bottom:48px;width:160px;height:52px;display:flex;background:var(--grey-btn);color:var(--white);font-family:"Montserrat",sans-serif;font-size:15px;align-items:center}
.plan.featured .details{left:84px;background:var(--navy)}
.plan .details span{flex:1;text-align:center}
.plan .details i{width:46px;height:52px;display:flex;align-items:center;justify-content:center;background:rgba(0,0,0,.2);font-style:normal}
.ribbon{position:absolute;left:-4px;top:-4px;width:100px;height:100px;overflow:hidden}
.ribbon span{position:absolute;left:-36px;top:26px;width:150px;height:26px;background:var(--red);transform:rotate(-45deg);color:var(--white);font-family:"Montserrat",sans-serif;font-size:10px;font-weight:600;line-height:26px;text-align:center}

/* why */
.why{top:1622px;height:520px}
.why-photo{position:absolute;left:0;top:0;width:600px;height:520px;background:linear-gradient(135deg,#3a5a86,#7f97b4 55%,#2d4a72)}
.why-play{position:absolute;left:245px;top:210px;width:96px;height:96px;border:3px solid var(--white);border-radius:50%;display:flex;align-items:center;justify-content:center}
.why-text{position:absolute;left:600px;top:0;width:600px;height:520px;background:var(--white);padding:44px 40px 0 32px}
.why-text h2{font-size:44px;font-weight:400;margin-bottom:28px}
.why-text p{font-family:"Montserrat",sans-serif;font-size:14px;line-height:22px;color:var(--muted);margin-bottom:22px}
.why-dots{position:absolute;left:642px;bottom:38px;display:flex;gap:8px}
.why-dots b{width:9px;height:9px;border-radius:50%;background:var(--navy)}
.why-dots b+b{background:#ccc}

/* steps */
.steps{top:2142px;height:409px}
.steps-line{position:absolute;left:60px;top:113px;width:1080px;height:2px;background:var(--line)}
.step{position:absolute;top:74px;width:80px;height:80px;border-radius:50%;background:#d4d4d4;color:var(--white);font-family:"Montserrat",sans-serif;font-size:24px;display:flex;align-items:center;justify-content:center}
.step.first{background:var(--navy)}
.step-stem{position:absolute;width:2px;background:var(--line)}
.step-note{position:absolute;width:160px;font-family:"Montserrat",sans-serif;font-size:13px;line-height:17px;color:var(--text);text-align:center}

/* call bar */
.callbar{top:2551px;height:133px;background:linear-gradient(90deg,var(--navy-dark),#2d5487 60%,#6f8db3)}
.callbar p{position:absolute;left:80px;top:54px;font-family:"Montserrat",sans-serif;font-size:19px;color:var(--white)}
.callbar p span{font-size:22px;text-transform:uppercase}
.callbar .btn{position:absolute;left:940px;top:40px;width:180px;height:52px;line-height:52px;background:var(--white);color:var(--navy)}

/* team */
.team{top:2684px;height:545px}
.team h2{position:absolute;left:0;width:1200px;top:60px;text-align:center;font-size:44px;font-weight:400}
.member{position:absolute;top:120px;width:250px}
.member .photo{height:315px;background:linear-gradient(180deg,#cfd6de,#8f9cab)}
.member.lead .photo{background:linear-gradient(180deg,#3d5d86,#243e63);position:relative}
.member .bio{position:absolute;left:64px;top:136px;width:122px;height:46px;border:2px solid var(--white);color:var(--white);font-family:"Montserrat",sans-serif;font-size:14px;line-height:42px;text-align:center}
.member h3{margin-top:18px;font-family:"Montserrat",sans-serif;font-size:19px;font-weight:500;color:var(--navy)}
.member p{margin-top:4px;font-family:"Montserrat",sans-serif;font-size:12px;color:var(--muted)}
.team-arrow{position:absolute;top:280px;font-size:26px;color:var(--ink)}

/* contact form */
.contact{top:3229px;height:346px;background:linear-gradient(90deg,#e9ebee,#f5f6f7)}
.contact-photo{position:absolute;left:48px;top:0;width:390px;height:346px;background:linear-gradient(180deg,#c9d7ea,#6f93c4)}
.contact h2{position:absolute;left:488px;top:46px;font-size:40px;font-weight:400}
.contact .intro{position:absolute;left:488px;top:110px;width:620px;font-family:"Montserrat",sans-serif;font-size:11.5px;line-height:17px;color:var(--muted)}
.field{position:absolute;height:42px;border:1px solid #d6d6d6;background:var(--white);font-family:"Montserrat",sans-serif;font-size:12px;color:#a9a9a9;padding:13px 12px}
.contact .btn{position:absolute;left:905px;top:272px;width:205px;height:58px;line-height:58px;background:var(--navy);color:var(--white)}

/* testimonial */
.testimonial{top:3575px;height:410px;text-align:center}
.testimonial h2{margin-top:40px;font-size:40px;font-weight:400}
.avatar{position:absolute;left:554px;top:110px;width:92px;height:92px;border-radius:50%;background:linear-gradient(180deg,#d9c3ad,#8a6a54)}
.avatar-ghost{position:absolute;top:128px;width:56px;height:56px;border-radius:50%;background:#d2d2d2}
.t-arrow{position:absolute;top:140px;font-size:22px}
.testimonial h3{position:absolute;left:0;width:1200px;top:222px;font-size:16px;font-weight:600;letter-spacing:1px}
.testimonial p{position:absolute;left:240px;width:720px;top:255px;font-family:"Montserrat",sans-serif;font-size:12.5px;line-height:19px;color:var(--muted);font-style:italic}

/* subscribe */
.subscribe{top:3985px;height:236px;background:linear-gradient(90deg,#f1f2f4,#e6e8eb)}
.subscribe h2{position:absolute;left:120px;top:36px;font-family:"Playfair Display",serif;font-size:66px;font-weight:400;color:var(--navy)}
.subscribe h3{position:absolute;left:120px;top:122px;font-family:"Playfair Display",serif;font-size:36px;font-weight:400;color:var(--navy-dark)}
.mail-circle{position:absolute;left:468px;top:60px;width:132px;height:132px;border-radius:50%;background:#8c8c8c;border:6px solid #dcdcdc;display:flex;align-items:center;justify-content:center}
.sub-field{position:absolute;left:600px;top:103px;width:480px;height:54px;background:var(--navy);border-radius:0 6px 6px 0;font-family:"Montserrat",sans-serif;font-size:14px;color:#dfe6ef;padding:18px 18px 0 16px}
.sub-field svg{position:absolute;right:18px;top:16px}

/* footer */
.site-footer{top:4221px;height:441px;background:linear-gradient(180deg,#2a3442,#1a2230 60%,#3b4655)}
.footer-box{position:absolute;left:420px;top:66px;width:440px;height:330px;background:rgba(255,255,255,.14);text-align:center;color:var(--white)}
.footer-box h2{margin-top:30px;font-size:40px;font-weight:400;letter-spacing:1px}
.f-row{position:absolute;display:flex;align-items:center;gap:12px;font-family:"Montserrat",sans-serif;font-size:13px;color:var(--white);text-align:left;line-height:18px}
.f-icon{width:46px;height:46px;border-radius:50%;background:var(--white);display:flex;align-items:center;justify-content:center;flex:none}
.socials{position:absolute;left:0;width:440px;top:262px;display:flex;justify-content:center;gap:10px}
.socials i{width:38px;height:38px;border-radius:50%;background:var(--white)}
.copyright{position:absolute;top:4662px;left:0;width:1200px;height:62px;background:var(--navy-dark);text-align:center;font-family:"Montserrat",sans-serif;font-size:13px;color:#b8c4d4;line-height:62px}
</style>
</head>
<body>

<header class="site-header">
  <div class="brand">
    <div class="brand-dot"></div>
    <div class="brand-name">LedgerPeak Analysts</div>
    <div class="brand-tag">OUTSOURCED FINANCIAL ANALYST PARTNER</div>
  </div>
  <div class="top-mail">
    <svg width="16" height="12" viewBox="0 0 16 12"><rect x="0.5" y="0.5" width="15" height="11" fill="none" stroke="#6d6d6d"/><path d="M1 1l7 6 7-6" fill="none" stroke="#6d6d6d"/></svg>
    info@ledgerpeak.example
  </div>
  <div class="top-phone">
    <svg width="20" height="20" viewBox="0 0 24 24"><path d="M6.6 10.8a15 15 0 006.6 6.6l2.2-2.2c.3-.3.7-.4 1-.2 1.1.4 2.3.6 3.6.6.6 0 1 .4 1 1V20c0 .6-.4 1-1 1A17 17 0 013 4c0-.6.4-1 1-1h3.5c.6 0 1 .4 1 1 0 1.3.2 2.5.6 3.6.1.3 0 .7-.2 1z" fill="#fff"/></svg>
    555-014-2290
  </div>
  <nav class="main-nav">
    <span class="active">Home</span><span>About Us</span><span>Products</span><span>Why Hire</span><span>Process</span><span>Contact Us</span>
  </nav>
</header>

<section class="hero" role="img" aria-label="Photo of an analyst holding a tablet showing financial charts">
  <h1>MORE THAN YOU EXPECT</h1>
  <p>Lorem ipsum dolor sit amet, consectetur adipiscing elit. Mauris sit amet congue ante. Nulla imperdiet velit eu sem sollicitudin.</p>
  <span class="btn">Get Started Now</span>
</section>

<section class="welcome">
  <h2>Welcome To LedgerPeak Analysts</h2>
  <p class="lead">LedgerPeak Analysts functions as an outsourced Financial Analyst partner for smaller, regional investment banks, private equity firms, business brokers, and mezzanine loan funds.</p>
  <p class="gap">We focus exclusively on lower middle-market clients.</p>
  <p class="gap">We believe Financial Models and Investment Memos are two of the most important deal support tools for executing private equity and investment banking transactions.</p>
  <span class="btn">Read More</span>
</section>

<section class="pricing">
  <div class="plan" style="left:79px">
    <div class="price">$3,500</div>
    <div class="tag">Financial Models</div>
    <ul><li>LBO</li><li>Growth Equity</li><li>Recap</li></ul>
    <div class="details"><span>DETAILS</span><i>»</i></div>
  </div>
  <div class="plan featured" style="left:432px;width:340px">
    <div class="ribbon"><span>BEST SELLER</span></div>
    <div class="price">$2,500</div>
    <div class="tag">Valuation Models</div>
    <ul><li>Discounted Cashflow</li><li>Comparable Company Analysis</li><li>Private Multiple Analysis</li></ul>
    <div class="details"><span>DETAILS</span><i>»</i></div>
  </div>
  <div class="plan" style="left:825px;width:293px">
    <div class="price">$3,500</div>
    <div class="tag">Investment Document</div>
    <ul><li>15-20 page Investment Memo</li><li>15-20 page Investor Powerpoint</li><li>40-50 page CIM</li></ul>
    <div class="details" style="left:66px"><span>DETAILS</span><i>»</i></div>
  </div>
</section>

<section class="why">
  <div class="why-photo" role="img" aria-label="Photo of a team meeting in a bright office, tinted blue">
    <div class="why-play"><svg width="30" height="34" viewBox="0 0 30 34"><path d="M4 2l24 15L4 32z" fill="#fff"/></svg></div>
  </div>
  <div class="why-text">
    <h2>Why Choose Us?</h2>
    <p>» We are much more cost-effective than hiring full-time Analyst staff.</p>
    <p>» We give You the ability to purchase Financial Models and Investment Memos on a "product-by-product" on-demand basis with standardized prices.</p>
    <p>» Cost of our Financial Models and Investment Memos is less expensive than other outsourced deal providers including investment bankers, attorneys, accountants and industry consultants.</p>
    <p>» We are highly responsive and expedient. We deliver Financial Models and Investment Memos in 72 hours or less.</p>
  </div>
  <div class="why-dots"><b></b><b></b></div>
</section>

<section class="steps">
  <div class="steps-line"></div>
  <!-- stems -->
  <div class="step-stem" style="left:187px;top:154px;height:255px"></div>
  <div class="step-stem" style="left:338px;top:0;height:74px"></div>
  <div class="step-stem" style="left:483px;top:154px;height:255px"></div>
  <div class="step-stem" style="left:637px;top:0;height:74px"></div>
  <div class="step-stem" style="left:782px;top:154px;height:255px"></div>
  <div class="step-stem" style="left:937px;top:0;height:74px"></div>
  <div class="step-stem" style="left:1082px;top:154px;height:255px"></div>

  <div class="step first" style="left:148px">1</div>
  <div class="step" style="left:299px">2</div>
  <div class="step" style="left:444px">3</div>
  <div class="step" style="left:598px">4</div>
  <div class="step" style="left:743px">5</div>
  <div class="step" style="left:898px">6</div>
  <div class="step" style="left:1043px">7</div>

  <p class="step-note" style="left:108px;top:178px;background:var(--white)">Call or email us a brief two sentence description of your deal project.</p>
  <p class="step-note" style="left:259px;top:6px;background:var(--white)">A LedgerPeak client service rep will contact you within 24 hours</p>
  <p class="step-note" style="left:404px;top:178px;background:var(--white)">To ensure confidentiality, we will request that you forward a copy of your Non-Disclosure Agreement.</p>
  <p class="step-note" style="left:558px;top:6px;background:var(--white)">In order for us to get our arms around the transaction we will email you a blank Sources &amp; Uses of Funds template.</p>
  <p class="step-note" style="left:703px;top:178px;background:var(--white)">You email us all of the basic information we would need to create your Financial Model including historical financials.</p>
  <p class="step-note" style="left:858px;top:6px;background:var(--white)">You email us all of the basic information we would need to create your Investment Memo.</p>
  <p class="step-note" style="left:1003px;top:178px;background:var(--white)">We email You a completed Financial Model or Investment Memo within 72 hours.</p>
</section>

<section class="callbar">
  <p>Contact us for information or any queries related to <span>Financial Investments</span></p>
  <span class="btn">Get Advice</span>
</section>

<section class="team">
  <h2>Our Team</h2>
  <span class="team-arrow" style="left:30px">‹</span>
  <span class="team-arrow" style="left:1150px">›</span>
  <div class="member lead" style="left:79px">
    <div class="photo" role="img" aria-label="Portrait of the managing partner with a blue overlay"><span class="bio">READ BIO</span></div>
    <h3>Owen Hale</h3><p>Managing Partner</p>
  </div>
  <div class="member" style="left:340px">
    <div class="photo" role="img" aria-label="Portrait of the managing director"></div>
    <h3>Nora Blake</h3><p>Managing Director</p>
  </div>
  <div class="member" style="left:605px">
    <div class="photo" role="img" aria-label="Portrait of the vice president"></div>
    <h3>Felix Amado</h3><p>Vice President</p>
  </div>
  <div class="member" style="left:869px">
    <div class="photo" role="img" aria-label="Portrait of the director"></div>
    <h3>Iris Lund</h3><p>Director</p>
  </div>
</section>

<section class="contact">
  <div class="contact-photo" role="img" aria-label="Photo of a smiling consultant holding a phone"></div>
  <h2>Contact Us</h2>
  <p class="intro">Consectetur adipiscing elit sed do eiusmod tempor incididunt ut labore et dolore magna aliqua. Ut enim ad minim veniam, quis nostrud exercitation ullamco laboris nisi ut.</p>
  <div class="field" style="left:488px;top:152px;width:622px">Name</div>
  <div class="field" style="left:488px;top:202px;width:306px">Email</div>
  <div class="field" style="left:804px;top:202px;width:306px">Telephone</div>
  <div class="field" style="left:488px;top:252px;width:406px;height:78px">Message</div>
  <span class="btn">Submit</span>
</section>

<section class="testimonial">
  <h2>Testimonial</h2>
  <span class="t-arrow" style="left:486px">‹</span>
  <div class="avatar-ghost" style="left:528px"></div>
  <div class="avatar-ghost" style="left:616px"></div>
  <div class="avatar" role="img" aria-label="Round portrait of the client giving the testimonial"></div>
  <span class="t-arrow" style="left:706px">›</span>
  <h3>LOREM IPSUM</h3>
  <p>"Lorem ipsum dolor sit amet, consectetur adipiscing elit. Maecenas ut est lacus. Fusce vitae sodales nibh. Vivamus auctor erat vitae risus consequat maximus. Quisque sodales vitae odio at malesuada. Vivamus fringilla, erat vitae maximus maximus, est mi porta dui, in ultrices nibh ipsum nec ligula."</p>
</section>

<section class="subscribe">
  <h2>Subscribe</h2>
  <h3>Newsletter</h3>
  <div class="mail-circle">
    <svg width="52" height="38" viewBox="0 0 52 38"><rect x="2" y="2" width="48" height="34" fill="none" stroke="#fff" stroke-width="3"/><path d="M3 3l23 18L49 3" fill="none" stroke="#fff" stroke-width="3"/></svg>
  </div>
  <div class="sub-field">Enter Email
    <svg width="22" height="22" viewBox="0 0 24 24"><path d="M2 11l20-9-7 20-3-8z" fill="none" stroke="#fff" stroke-width="2" stroke-linejoin="round"/></svg>
  </div>
</section>

<footer class="site-footer" role="img" aria-label="Night photo of a city skyline by the water">
  <div class="footer-box">
    <h2>CONTACT US</h2>
    <div class="f-row" style="left:50px;top:110px">
      <span class="f-icon"><svg width="20" height="20" viewBox="0 0 24 24"><path d="M6.6 10.8a15 15 0 006.6 6.6l2.2-2.2c.3-.3.7-.4 1-.2 1.1.4 2.3.6 3.6.6.6 0 1 .4 1 1V20c0 .6-.4 1-1 1A17 17 0 013 4c0-.6.4-1 1-1h3.5c.6 0 1 .4 1 1 0 1.3.2 2.5.6 3.6.1.3 0 .7-.2 1z" fill="#123a6b"/></svg></span>555-014-2290
    </div>
    <div class="f-row" style="left:200px;top:110px">
      <span class="f-icon"><svg width="20" height="15" viewBox="0 0 20 15"><rect x="1" y="1" width="18" height="13" fill="none" stroke="#123a6b" stroke-width="2"/><path d="M1 1l9 7 9-7" fill="none" stroke="#123a6b" stroke-width="2"/></svg></span>info@ledgerpeak.example
    </div>
    <div class="f-row" style="left:50px;top:180px">
      <span class="f-icon"><svg width="16" height="22" viewBox="0 0 16 22"><path d="M8 1a7 7 0 00-7 7c0 5 7 13 7 13s7-8 7-13a7 7 0 00-7-7z" fill="#123a6b"/><circle cx="8" cy="8" r="2.5" fill="#fff"/></svg></span>120 Harbor Street, Suite 400,<br>Riverton, MA 02100
    </div>
    <div class="socials"><i></i><i></i><i></i><i></i></div>
  </div>
</footer>
<div class="copyright">© LedgerPeak Analysts - 2017. All rights reserved.</div>

</body>
</html>
```